Coralbay Realty Letterhead

Coralbay Realty Guan
418 Maru Tasi Loop, Ste B207
Tumon, GU. 96928

Industry/Entity Type

Real Estate

Font styles to use
Serif

Colors

Designer to choose colors to be used in the design.

```html
<!DOCTYPE html>
<html lang="en">
<head>
<meta charset="utf-8">
<title>Coralbay Realty Letterhead</title>
<link href="https://fonts.googleapis.com/css2?family=Montserrat:wght@400;500;600;700&family=Open+Sans:wght@600&family=Questrial&display=swap" rel="stylesheet">
<style>
  :root {
    --bg: #e4e5e8;
    --paper: #ffffff;
    --brand-blue: #1a8fd0;
    --name-blue: #5fc0e8;
    --rule-blue: #3aa6dc;
    --text-grey: #5c5c5c;
    --body-grey: #6a6a6a;
    --sign-fill: #ececee;
  }
  * { box-sizing: border-box; margin: 0; padding: 0; }
  html, body {
    width: 1023px; height: 1200px; overflow: hidden;
    background: var(--bg);
  }
  .letterhead {
    position: absolute; left: 91px; top: 12px;
    width: 840px; height: 1176px;
    background: var(--paper);
    box-shadow: 0 6px 18px rgba(0,0,0,0.12);
  }
  .brand-name {
    position: absolute; left: 55px; top: 124px;
    font-family: "Montserrat", sans-serif; font-weight: 500;
    font-size: 31px; letter-spacing: 1px; color: var(--brand-blue);
    display: flex; align-items: center; gap: 10px;
  }
  .brand-dot { width: 14px; height: 14px; border-radius: 50%; background: var(--brand-blue); }
  .header-rule {
    position: absolute; left: 55px; top: 167px;
    width: 573px; height: 1.5px; background: var(--rule-blue);
  }
  .office {
    position: absolute; right: 60px; top: 108px; text-align: right;
    font-family: "Montserrat", sans-serif; color: var(--text-grey);
  }
  .office-name { font-weight: 600; font-size: 19.5px; color: var(--brand-blue); margin-bottom: 4px; }
  .office-line { font-size: 15.5px; line-height: 20px; }
  .recipient {
    position: absolute; left: 55px; top: 259px;
    font-family: "Montserrat", sans-serif; color: var(--text-grey);
  }
  .recipient-name { font-weight: 700; font-size: 25px; color: var(--name-blue); letter-spacing: 0.3px; margin-bottom: 10px; }
  .recipient-line { font-size: 14.5px; line-height: 18px; margin-bottom: 8px; }
  .recipient-address { font-size: 14.5px; line-height: 18px; }
  .letter-date {
    position: absolute; right: 60px; top: 360px;
    font-family: "Open Sans", sans-serif; font-weight: 600;
    font-size: 17px; color: var(--text-grey);
  }
  .letter-body {
    position: absolute; left: 55px; top: 419px; width: 730px;
    font-family: "Questrial", sans-serif; font-size: 14.2px;
    line-height: 18.4px; color: var(--body-grey); text-align: justify;
  }
  .letter-body p { margin-bottom: 18.4px; }
  .letter-body p.gap-after { margin-bottom: 36px; }
  .signer-title {
    position: absolute; left: 57px; top: 829px;
    font-family: "Questrial", sans-serif; font-size: 26px; color: var(--text-grey);
  }
  .signature {
    position: absolute; left: 59px; top: 901px;
    width: 219px; height: 145px; background: var(--sign-fill);
  }
</style>
</head>
<body>
  <main class="letterhead">
    <div class="brand-name"><span class="brand-dot"></span>Coralbay Realty</div>
    <div class="header-rule"></div>

    <div class="office">
      <div class="office-name">Coralbay Realty Guan</div>
      <div class="office-line">418 Maru Tasi Loop, Ste B207</div>
      <div class="office-line">Tumon, GU. 96928</div>
    </div>

    <div class="recipient">
      <div class="recipient-name">LENA MARSH</div>
      <div class="recipient-line">0147-258-369</div>
      <div class="recipient-line">hello@tidewaymail.com</div>
      <div class="recipient-address">5678 Harbor View Ln. Suite<br>45 Austin, TX 7010</div>
    </div>

    <div class="letter-date">12 December, 2023</div>

    <div class="letter-body">
      <p>Lorem ipsum dolor sit amet, consectetuer adipiscing elit, sed diam nonummy nibh euismod tincidunt ut laoreet dolore magna aliquam erat volutpat. Ut wisi enim ad minim veniam, quis nostrud exerci tation ullamcorper suscipit lobortis nisl ut aliquip ex ea commodo consequat. Duis autem vel eum iriure dolor in hendrerit in vulputate velit esse molestie consequat, vel illum dolore eu feugiat nulla facilisis at vero eros et accumsan et iusto odio dignissim qui blandit praesent luptatum zzril delenit augue duis dolore te feugait nulla facilisi.</p>
      <p class="gap-after">Lorem ipsum dolor sit amet, cons ectetuer adipiscing elit, sed diam nonummy nibh euismod tincidunt ut laoreet dolore magna aliquam erat volutpat. Ut wisi enim ad minim veniam, quis nostrud exerci tation ullamcorper suscipit lobortis nisl ut aliquip ex ea commodo consequat.<br>Lorem ipsum dolor sit amet, consectetuer adipiscing elit, sed diam nonummy nibh euismod tincidunt ut laoreet dolore magna aliquam erat</p>
      <p>Lorem ipsum dolor sit amet, cons ectetuer adipiscing elit, sed diam nonummy nibh euismod tincidunt ut laoreet dolore magna aliquam erat volutpat. Ut wisi enim ad minim veniam, quis nostrud exerci tation ullamcorper suscipit lobortis nisl ut aliquip ex ea commodo consequat. Lorem ipsum dolor sit zamet, consectetuer adipiscing elit, sed diam nonummy nibh euismod tincidunt ut laoreet dolore magna aliquam erat volutpat. Ut wisi enim ad minim veniam, quis nostrud exerci tation ullamcorper suscipit lobortis nisl ut aliquip ex ea commodo consequat. Duis autem vel eum iriure.</p>
    </div>

    <div class="signer-title">Managing Director</div>
    <div class="signature" role="img" aria-label="Handwritten signature of the managing director"></div>
  </main>
</body>
</html>
```